Concrete Finishing business needs new business card and a logo design

We are a family owned and operated, concrete finishing business. 2020 marks our 33 rd year in business. We operate under Harold P. Mercer and Sons Concrete Contractors Ltd. Harold P was my father and founder of the company. We usually shorten the name and use H P Mercer & Sons Ltd. Most people in the Concrete Finishing industry tend to know us by our last name 'Mercer' . in honour of our father, we would still like to have his name on the cards and logo but are open to shortening it to H.P (maybe in a small font with the H on top of the P ) and focusing more on the "Mercer & Sons."....Or maybe something with just the initials HPM...or if you could use the "P" and somehow incorporate an artistic drawing/shape of a 'power trowel' (what we use apply a smooth finish to the concrete with) but still visually see that its a P, would be cool. Would like to see designs using Black with silver or grey lettering but are open to other ideas. Seen a business card online with the front of the business card looking like concrete and with just the word CONCRETE on it... On the back was the company name , address and contact info of the company....looked really good! i clicked doubled sided in case of something like that but we are open to just single sided as well. After viewing some of the designs, maybe a pop of colour would be nice ... open to any ideas and colours.😊

Target Market(s)

Construction

```html
<!DOCTYPE html>
<html lang="en">
<head>
<meta charset="utf-8">
<title>HP Mercer &amp; Sons – Business Card</title>
<link rel="stylesheet" href="https://fonts.googleapis.com/css2?family=Montserrat+Alternates:wght@700&family=Arimo:wght@400;700&display=swap">
<style>
  :root {
    --ink: #0a0a0a;
    --paper: #ffffff;
    --accent: #f28a00;
    --backdrop: #e9e6e1;
    --text: #1a1a1a;
  }
  * { box-sizing: border-box; margin: 0; padding: 0; }
  html, body { width: 1200px; height: 900px; overflow: hidden; }
  body { background: var(--backdrop); position: relative; font-family: "Arimo", Arial, sans-serif; color: var(--text); }

  .card { position: absolute; width: 620px; height: 354px; overflow: hidden; box-shadow: 0 6px 18px rgba(0,0,0,.18); }
  .card--front { left: 60px; top: 70px; background: var(--ink); }
  .card--back  { left: 520px; top: 476px; background: var(--paper); }

  .brand { display: flex; align-items: center; font-family: "Montserrat Alternates", "Arimo", sans-serif; font-weight: 700; white-space: nowrap; }
  .brand__square { background: var(--accent); flex: none; }
  .brand--front { position: absolute; left: 0; right: 0; top: 0; bottom: 0; justify-content: center; gap: 18px; color: var(--paper); font-size: 38px; }
  .brand--front .brand__square { width: 42px; height: 42px; }
  .brand--back { position: absolute; right: 30px; top: 62px; gap: 10px; color: var(--ink); font-size: 22px; }
  .brand--back .brand__square { width: 20px; height: 20px; }

  .wave { position: absolute; left: 0; top: 0; width: 620px; height: 354px; }
  .wave__band { fill: var(--ink); }
  .wave__swoosh { fill: var(--accent); }

  .person { position: absolute; left: 40px; top: 36px; }
  .person__name { font-family: "Montserrat Alternates", "Arimo", sans-serif; font-weight: 700; color: var(--accent); font-size: 19px; letter-spacing: .5px; text-transform: uppercase; }
  .person__role { font-size: 15px; margin-top: 2px; }

  .contact { position: absolute; left: 40px; top: 100px; list-style: none; font-size: 14.5px; line-height: 22px; }
  .contact li { display: flex; align-items: center; gap: 9px; }
  .contact svg { width: 15px; height: 15px; flex: none; fill: none; stroke: var(--accent); stroke-width: 2; stroke-linejoin: round; stroke-linecap: round; }
  .contact svg .solid { fill: var(--accent); stroke: none; }

  .address { position: absolute; left: 40px; top: 200px; font-style: normal; font-size: 15px; line-height: 21px; }

  .tagline { position: absolute; right: 26px; bottom: 26px; color: var(--accent); font-size: 13px; letter-spacing: .6px; text-transform: uppercase; }
</style>
</head>
<body>

<section class="card card--front" aria-label="Card front">
  <div class="brand brand--front">
    <span class="brand__square"></span>
    <span class="brand__name">HP Mercer &amp; Sons</span>
  </div>
</section>

<section class="card card--back" aria-label="Card back">
  <svg class="wave" viewBox="0 0 620 354" aria-hidden="true">
    <path class="wave__swoosh" d="M0,282 C170,286 360,250 520,162 C380,262 180,300 0,300 Z"/>
    <path class="wave__band" d="M0,300 C180,300 380,250 620,110 L620,354 L0,354 Z"/>
  </svg>

  <div class="person">
    <p class="person__name">Daniel Hartley</p>
    <p class="person__role">Managing Director</p>
  </div>

  <ul class="contact">
    <li>
      <svg viewBox="0 0 16 16" aria-label="Mobile"><rect x="4" y="1.5" width="8" height="13" rx="1.5"/><circle class="solid" cx="8" cy="12" r="0.9"/></svg>
      (709)555-0142
    </li>
    <li>
      <svg viewBox="0 0 16 16" aria-label="Phone"><path d="M3 2.5 L6 2.5 L7 5.5 L5.3 6.7 C6.2 8.6 7.4 9.8 9.3 10.7 L10.5 9 L13.5 10 L13.5 13 C8 13.5 2.5 8 3 2.5 Z"/></svg>
      (709)555-0187
    </li>
    <li>
      <svg viewBox="0 0 16 16" aria-label="Fax"><rect x="4.5" y="1.5" width="7" height="4"/><rect x="1.5" y="5.5" width="13" height="6" rx="1"/><rect x="4.5" y="9.5" width="7" height="5"/></svg>
      (709)555-0163
    </li>
    <li>
      <svg viewBox="0 0 16 16" aria-label="Email"><rect x="1.5" y="3.5" width="13" height="9"/><path d="M1.5 3.5 L8 9 L14.5 3.5"/></svg>
      hpmercer@fieldmail.com
    </li>
  </ul>

  <address class="address">
    P.O.Box 41, Site 9, RR#2<br>
    Harbour Bend, NL<br>
    A0B 2C0
  </address>

  <div class="brand brand--back">
    <span class="brand__square"></span>
    <span class="brand__name">HP Mercer &amp; Sons</span>
  </div>

  <p class="tagline">Specializing in concrete floor finishing</p>
</section>

</body>
</html>
```